Motor Mate 4x6 Flyer

Need 4 x 6 Flyer with following language:

Willow Crest Motor Mate
Our Motor Mate Will Come to Your Home
Our Motor Mate will Drive Your Car to Nearest Gas Station
Our Motor Mate will Fill-up Your Car with Gas
Our Motor Mate will Immediately Return Your Car
Your Car Covered with $100k of Commercial Insurance
Member Dunmore Chamber of Commerce / Honest Merchant League
www.willowcrestmotormate.example

Place logos of Vortan, Brenn & Dorvane on Left Side of Flyer starting at top left corner, mid left side, left bottom corner.
Place logos of BoltNest, 12-Forty, Tesmira on opposite side right.....
Place Willow Crest Motor Mate Logo on both sides of very top that says Willow Crest Motor Mate

Target Market(s)

Upscale Home Owners

Font styles to use
Sans Serif

Colors
F0912C
F2A743
F7CA91
FBE8D2
FDF5EE

Requirements
Must have
• Flyer Must be Bright Orange

```html
<!DOCTYPE html>
<html lang="en">
<head>
<meta charset="utf-8">
<title>Willow Crest Motor Mate Flyer</title>
<link rel="stylesheet" href="https://fonts.googleapis.com/css2?family=Jost:wght@300;400;500;600;700&family=Montserrat:wght@900&display=swap">
<style>
  :root {
    --orange: #F0912C;
    --amber: #F2A743;
    --peach: #F7CA91;
    --cream: #FBE8D2;
    --ink: #000000;
    --pill: #1E1E1E;
    --red: #E0282E;
    --gold: #F5B04A;
  }
  * { margin: 0; padding: 0; box-sizing: border-box; }
  html, body { width: 866px; height: 1200px; overflow: hidden; background: #fff; }
  .flyer {
    position: relative; width: 866px; height: 1200px;
    font-family: "Jost", sans-serif; color: var(--ink);
  }
  .frame {
    position: absolute; left: 34px; top: 1px; width: 800px; height: 1198px;
    border: 2px solid var(--ink); overflow: hidden; background: var(--peach);
  }
  .band { position: absolute; left: 0; width: 100%; }
  .band--brands { top: 0; height: 90px; background: var(--orange); border-bottom: 1.5px solid var(--ink); }
  .band--header { top: 102px; height: 268px; background: var(--amber); }
  .band--insurance { top: 862px; height: 96px; background: var(--orange); }
  .band--member { top: 983px; height: 95px; background: var(--amber); }
  .band--web { top: 1103px; height: 96px; background: var(--orange); border-top: 1.5px solid var(--ink); }

  .brand {
    position: absolute; top: 32px; font-weight: 700; font-size: 18px; line-height: 1;
    display: flex; align-items: center; gap: 5px; white-space: nowrap;
  }
  .brand__dot { width: 11px; height: 11px; border-radius: 50%; background: currentColor; }
  .brand--brenn { left: 42px; color: #E4202A; }
  .brand--dorvane { left: 132px; color: #1B5FA8; }
  .brand--vortan { left: 228px; color: #E0282E; font-size: 30px; top: 26px; }
  .brand--boltnest { left: 538px; color: #B3131A; font-size: 17px; }
  .brand--tesmira { left: 640px; color: #1C4E9A; font-size: 17px; }
  .brand--twelve { left: 720px; color: #0A7A3C; font-size: 17px; }

  .can { position: absolute; border-radius: 4px; background: var(--red); opacity: .85; }
  .can--left { left: 93px; top: 93px; width: 43px; height: 60px; }
  .can--right { left: 669px; top: 87px; width: 44px; height: 62px; }
  .mark-label {
    position: absolute; font-weight: 500; font-size: 21px; letter-spacing: 1px;
    color: var(--ink); white-space: nowrap;
  }
  .mark-label--left { left: 34px; top: 164px; }
  .mark-label--right { left: 622px; top: 158px; }

  .title {
    position: absolute; left: 0; width: 100%; text-align: center;
    font-family: "Montserrat", sans-serif; font-weight: 900; font-size: 62px;
    top: 94px; letter-spacing: -1px; line-height: 1;
  }
  .subtitle {
    position: absolute; left: 0; width: 100%; text-align: center;
    font-weight: 300; font-size: 64px; top: 160px; line-height: 1; letter-spacing: 0;
  }

  .step {
    position: absolute; left: 71px; width: 658px; height: 52px; background: var(--orange);
    display: flex; align-items: center; font-size: 21px; font-weight: 400; list-style: none;
  }
  .step__num {
    width: 32px; height: 32px; border-radius: 50%; background: var(--ink); color: #fff;
    display: flex; align-items: center; justify-content: center; font-size: 17px;
    margin: 0 10px 0 7px; flex: none;
  }
  .step--1 { top: 422px; }
  .step--2 { top: 534px; }
  .step--3 { top: 646px; }
  .step--4 { top: 759px; left: 74px; width: 652px; }

  .pill {
    position: absolute; background: var(--pill); border-radius: 30px;
    display: flex; align-items: center; justify-content: center; white-space: nowrap;
  }
  .pill--insurance { left: 32px; top: 19px; width: 736px; height: 58px; background: var(--ink);
    color: var(--gold); font-size: 25px; letter-spacing: .5px; }
  .pill--insurance strong { color: #fff; font-weight: 700; margin: 0 8px; }
  .pill--member { left: 22px; top: 21px; width: 756px; height: 54px;
    font-weight: 700; font-size: 21px; color: var(--orange); }
  .pill--member .league { color: #fff; margin-left: 8px; }
  .pill--member .sep { color: #fff; margin-left: 8px; font-weight: 400; }
  .pill--web { left: 188px; top: 16px; width: 423px; height: 62px;
    font-weight: 700; font-size: 22px; color: #fff; }
  .pill--web .accent { color: var(--gold); }
</style>
</head>
<body>
<div class="flyer">
  <div class="frame">
    <header class="band band--brands">
      <span class="brand brand--brenn"><span class="brand__dot"></span>Brenn</span>
      <span class="brand brand--dorvane">Dorvane</span>
      <span class="brand brand--vortan">Vortan</span>
      <span class="brand brand--boltnest"><span class="brand__dot"></span>BoltNest</span>
      <span class="brand brand--tesmira">Tesmira</span>
      <span class="brand brand--twelve">12-Forty</span>
    </header>

    <section class="band band--header">
      <div class="can can--left" role="img" aria-label="Motor Mate mascot fuel can"></div>
      <div class="mark-label mark-label--left">MOTOR MATE</div>
      <div class="can can--right" role="img" aria-label="Motor Mate mascot fuel can"></div>
      <div class="mark-label mark-label--right">MOTOR MATE</div>
      <h1 class="title">WILLOW CREST</h1>
      <div class="subtitle">MOTOR MATE</div>
    </section>

    <ol>
      <li class="step step--1"><span class="step__num">1</span>Our Motor Mate Will Come to Your Home.</li>
      <li class="step step--2"><span class="step__num">2</span>Our Motor Mate will Drive Your Car to Nearest Gas Station.</li>
      <li class="step step--3"><span class="step__num">3</span>Our Motor Mate will Fill-up Your Car with Gas.</li>
      <li class="step step--4"><span class="step__num">4</span>Our Motor Mate will Immediately Return Your Car.</li>
    </ol>

    <section class="band band--insurance">
      <div class="pill pill--insurance">Your Car Covered with <strong>$100k</strong> of Commercial Insurance</div>
    </section>

    <section class="band band--member">
      <div class="pill pill--member">Member Dunmore Chamber of Commerce<span class="sep">/</span><span class="league">Honest Merchant League</span></div>
    </section>

    <footer class="band band--web">
      <div class="pill pill--web"><span class="accent">www.</span>willowcrestmotormate<span class="accent">.example</span></div>
    </footer>
  </div>
</div>
</body>
</html>
```